Brindle Logistics Business Card Design

We are a trucking and warehousing company. We run freight in the US manly from the Pacific NW to TX and back up the the PNW. We also do warehousing where we store, move, and distribute freight. Looking for a clean and modern design of business card. We would like to look rich and elegant. Attached is our logo.

Industry/Entity Type

Trucking Company

Contact Information for Business Card

Looking for a clean and modern design of business card. We would like to look rich and elegant.

Font styles to use
Sans Serif

Colors

Designer to choose colors to be used in the design.

Requirements
Must have
• logo but it should not dominate the card
Should not have
• logo should not dominate the card

```html
<!DOCTYPE html>
<html lang="en">
<head>
<meta charset="utf-8">
<title>Brindle Logistics Business Card</title>
<link href="https://fonts.googleapis.com/css2?family=Arimo:wght@400;700&display=swap" rel="stylesheet">
<style>
  :root {
    --stage: #2a2a2a;
    --card: #1d1d1f;
    --card-deep: #141415;
    --pattern-a: #262628;
    --pattern-b: #1a1a1c;
    --brand-blue: #1a7fd4;
    --ink-white: #f4f4f4;
  }
  * { box-sizing: border-box; margin: 0; padding: 0; }
  html, body {
    width: 1200px; height: 1189px; overflow: hidden;
    background: var(--stage);
    font-family: "Arimo", Arial, sans-serif;
  }
  .canvas { position: relative; width: 1200px; height: 1189px; }
  .card {
    position: absolute; width: 900px; height: 514px;
    border-radius: 30px; overflow: hidden;
    box-shadow: 0 18px 40px rgba(0,0,0,.55);
  }
  .card--back { left: 60px; top: 50px; }
  .card--front { left: 240px; top: 620px; background: linear-gradient(160deg, var(--card) 0%, var(--card-deep) 100%); }

  .back-pattern {
    position: absolute; inset: 0;
    background: radial-gradient(ellipse at 60% 40%, var(--pattern-a) 0%, var(--pattern-b) 80%);
  }
  .back-brand {
    position: absolute; right: 70px; top: 150px;
    display: flex; align-items: center; gap: 10px;
  }
  .brand-dot { width: 22px; height: 22px; border-radius: 50%; background: var(--brand-blue); }
  .back-brand .brand-name { color: var(--ink-white); font-weight: 700; font-size: 18px; letter-spacing: 1.5px; }

  .front-brand {
    position: absolute; left: 60px; top: 86px;
    display: flex; align-items: center; gap: 18px;
  }
  .front-brand .brand-dot { width: 54px; height: 54px; }
  .front-brand .brand-name { color: var(--ink-white); font-weight: 700; font-size: 40px; letter-spacing: 2px; }

  .divider {
    position: absolute; left: 60px; right: 60px; top: 330px;
    height: 2px; background: var(--brand-blue);
  }
  .person { position: absolute; left: 60px; top: 256px; }
  .person-name { color: var(--brand-blue); font-weight: 700; font-size: 30px; line-height: 1.1; }
  .person-title { color: var(--ink-white); font-size: 24px; margin-top: 4px; }

  .contacts { position: absolute; left: 60px; top: 352px; list-style: none; }
  .contacts li {
    display: flex; align-items: center; gap: 14px;
    color: var(--ink-white); font-size: 24px; height: 42px;
  }
  .contact-icon { width: 30px; height: 30px; flex: none; }

  .address {
    position: absolute; right: 70px; top: 352px;
    color: var(--ink-white); font-size: 22px; line-height: 1.45; text-align: left;
  }
</style>
</head>
<body>
<main class="canvas">
  <section class="card card--back" aria-label="Card back">
    <div class="back-pattern" role="img" aria-label="Tone-on-tone pattern of repeated bird-head motifs in dark grey"></div>
    <div class="back-brand">
      <span class="brand-dot"></span>
      <span class="brand-name">BRINDLE LOGISTICS</span>
    </div>
  </section>

  <section class="card card--front" aria-label="Card front">
    <div class="front-brand">
      <span class="brand-dot"></span>
      <span class="brand-name">BRINDLE LOGISTICS, LLC</span>
    </div>

    <div class="person">
      <p class="person-name">Dale Morrow</p>
      <p class="person-title">President &amp; CEO</p>
    </div>

    <div class="divider"></div>

    <ul class="contacts">
      <li>
        <svg class="contact-icon" viewBox="0 0 30 30" aria-hidden="true">
          <circle cx="15" cy="15" r="13.5" fill="none" stroke="var(--brand-blue)" stroke-width="2"/>
          <path d="M10 9.5c1-1 2-1 2.6 0l1.2 2c.4.7.2 1.4-.4 1.9l-.8.6c.7 1.6 1.8 2.7 3.4 3.4l.6-.8c.5-.6 1.2-.8 1.9-.4l2 1.2c1 .6 1 1.6 0 2.6-1.2 1.2-3 1.4-5 .3-2.6-1.4-4.5-3.3-5.9-5.9-1.1-2-.9-3.8.4-4.9z" fill="var(--brand-blue)"/>
        </svg>
        <span>+01 5550 1234</span>
      </li>
      <li>
        <svg class="contact-icon" viewBox="0 0 30 30" aria-hidden="true">
          <circle cx="15" cy="15" r="13.5" fill="none" stroke="var(--brand-blue)" stroke-width="2"/>
          <rect x="8" y="10" width="14" height="10" rx="1" fill="var(--brand-blue)"/>
          <path d="M8.5 10.5 15 16l6.5-5.5" fill="none" stroke="var(--card)" stroke-width="1.4"/>
        </svg>
        <span>info@brindlefreight.com</span>
      </li>
      <li>
        <svg class="contact-icon" viewBox="0 0 30 30" aria-hidden="true">
          <circle cx="15" cy="15" r="13.5" fill="none" stroke="var(--brand-blue)" stroke-width="2"/>
          <g fill="none" stroke="var(--brand-blue)" stroke-width="1.4">
            <circle cx="15" cy="15" r="7.5"/>
            <ellipse cx="15" cy="15" rx="3.2" ry="7.5"/>
            <path d="M7.5 15h15M8.5 11.5h13M8.5 18.5h13"/>
          </g>
        </svg>
        <span>www.brindlefreight.com</span>
      </li>
    </ul>

    <address class="address">
      PO BOX 480, Harbor Road<br>
      3rd Lane, Tacoma
    </address>
  </section>
</main>
</body>
</html>
```